Modern Billboard Ad for Criminal Defense Firm

10.5 x 36 We're looking for something to set us apart from the local competition. Looking for sleek and modern. We're a mid-sized firm in a small market city. We want to give the artist room to be creative on this one.
Thanks

Target Market(s)

Adult clients who have been charged with a crime/DWI

Industry/Entity Type

legal

Font styles to use
Serif
Sans Serif

Requirements
Must have
• Needs to have the firm name in large lettering. Law Offices of Marcus T Whitfield. “PLLC” does not have to be included. Phone number of (555) 384-1927 should be included but not the main focus.
Nice to have
• A call to action or something similar. “Don’t go it alone, call today.”, “ Arrested?”

```html
<!DOCTYPE html>
<html lang="en">
<head>
<meta charset="utf-8">
<title>Whitfield Law Billboard</title>
<link href="https://fonts.googleapis.com/css2?family=Barlow+Condensed:ital,wght@1,600;1,800&family=Poppins:wght@700&family=Nothing+You+Could+Do&display=swap" rel="stylesheet">
<style>
  :root {
    --navy: #0f1d3f;
    --navy-line: #1d2f5c;
    --gold: #f7b80f;
    --white: #ffffff;
    --page: #e4e5e8;
    --badge-dark: #231f20;
    --badge-blue: #27aee3;
    --photo-grey: #8c8c8c;
  }
  * { margin: 0; padding: 0; box-sizing: border-box; }
  html, body { width: 1200px; height: 888px; overflow: hidden; background: var(--page); }
  .billboard {
    position: absolute; left: 40px; top: 320px;
    width: 1120px; height: 248px;
    background: var(--white);
    box-shadow: 0 8px 22px rgba(0,0,0,.28);
    overflow: hidden;
  }
  .billboard-art { position: absolute; inset: 0; }
  .call-to-action {
    position: absolute; left: 170px; top: 24px; width: 220px;
    font-family: "Nothing You Could Do", cursive;
    color: var(--white); font-size: 13px; line-height: 27px;
    text-align: center; white-space: nowrap;
  }
  .phone-pill {
    position: absolute; left: 187px; top: 163px; width: 166px; height: 33px;
    border-radius: 17px; background: var(--gold); color: var(--navy);
    font-family: "Poppins", sans-serif; font-weight: 700; font-size: 16px;
    display: flex; align-items: center; justify-content: center;
  }
  .firm-name {
    position: absolute; left: 420px; top: 38px; width: 330px;
    transform: rotate(-6deg); transform-origin: right center;
    font-family: "Barlow Condensed", sans-serif; font-style: italic;
    text-align: right; line-height: .9; white-space: nowrap;
  }
  .firm-name .intro { display: block; color: var(--gold); font-weight: 600; font-size: 44px; padding-right: 12px; }
  .firm-name .first { display: block; color: var(--gold); font-weight: 800; font-size: 56px; padding-right: 30px; }
  .firm-name .last {
    display: block; color: var(--white); font-weight: 800; font-size: 68px;
    text-shadow: 2px 3px 4px rgba(0,0,0,.35);
  }
</style>
</head>
<body>
  <div class="billboard">
    <svg class="billboard-art" width="1120" height="248" viewBox="0 0 1120 248">
      <path d="M65 0 H800 V170 Q800 178 794 184 L738 248 H0 V65 Z" fill="var(--navy)"/>
      <rect x="18" y="22" width="142" height="204" fill="var(--badge-blue)"/>
      <rect x="21" y="25" width="136" height="172" fill="var(--badge-dark)"/>
      <path d="M177 0 V112 Q177 127 192 127 H355 Q363 127 369 121 L448 42 Q454 36 454 28 V0" fill="none" stroke="var(--gold)" stroke-width="1.2"/>
      <path d="M177 248 L213 218 H331 Q339 218 339 226 V248" fill="none" stroke="var(--gold)" stroke-width="1.2"/>
      <path d="M292 88 L296 114 L302 107 L311 121 L316 117 L307 103 L316 101 Z" fill="none" stroke="var(--white)" stroke-width="1.6" stroke-linejoin="round"/>
      <path d="M832 76 L885 23 H1028 Q1043 23 1043 38 V172 L981 234 H846 Q832 234 832 220 Z" fill="var(--gold)"/>
      <path d="M860 40 Q875 0 925 0 Q975 0 985 40 L1035 95 V190 L985 234 H846 Q832 234 832 220 V110 Z" fill="var(--photo-grey)" role="img" aria-label="Black and white portrait of the attorney in a vest and tie, jacket over his shoulder"/>
      <path d="M1025 248 V201 L1120 104" fill="none" stroke="var(--navy-line)" stroke-width="1.2"/>
      <path d="M1089 248 L1120 219" fill="none" stroke="var(--navy-line)" stroke-width="1.2"/>
    </svg>

    <p class="call-to-action">&quot;Don't go it alone, call<br>today.&quot;, &quot; Arrested?&quot;</p>
    <div class="phone-pill">(555) 384-1927</div>

    <h1 class="firm-name">
      <span class="intro">Law Offices of</span>
      <span class="first">Marcus</span>
      <span class="last">T Whitfield</span>
    </h1>
  </div>
</body>
</html>
```